U.S. Popcorn company needs business cards

We are a popcorn company that manufactures popcorn and sells it to grocery stores worldwide. Our theme is "Americana" and our logo is Kettle Mesa Byway which is the most famous highway in the U.S.

We would like the design to be simple and to use both sides. On the back side we would like to see just the logo and website. The front would be normal details

Target Market(s)

Wholesalers, grocers and distributors

Industry/Entity Type

Manufacture

Contact Information for Business Card

Business name: Kettle Mesa Popcorn
Phone: +1 555 014 2286
Email: Dale@kettlemesapopcorn.com
website: www.kettlemesapopcorn.com
Tag Line: "Crafted with a crunch"
Name: Dale Whitcombe
Title: Founder/President

Requirements
Must have
• Either this design should be fun or clean and simple. I will let you show me your thougths.
Nice to have
• Anything that ties in the real Kettle Mesa Byway.
• Colors might need to be red, white and blue incorporated.
Should not have
• Not be too busy.

```html
<!DOCTYPE html>
<html lang="en">
<head>
<meta charset="utf-8">
<title>Kettle Mesa Popcorn — Business Cards</title>
<link rel="stylesheet" href="https://fonts.googleapis.com/css2?family=Open+Sans:wght@400;600&family=Noto+Serif:wght@400&display=swap">
<style>
  :root {
    --stage: #000000;
    --card-red: #9c232b;
    --card-navy: #172a54;
    --ink-white: #ffffff;
    --ink-soft: #f1e6e6;
    --divider: rgba(255, 255, 255, 0.35);
  }
  * { margin: 0; padding: 0; box-sizing: border-box; }
  html, body {
    width: 1200px;
    height: 900px;
    overflow: hidden;
    background: var(--stage);
  }
  .stage {
    position: relative;
    width: 1200px;
    height: 900px;
    font-family: "Open Sans", Arial, sans-serif;
    color: var(--ink-white);
  }
  .card {
    position: absolute;
    top: 271px;
    width: 457px;
    height: 282px;
    border-radius: 14px;
  }
  .card--front { left: 137px; background: var(--card-red); }
  .card--back  { left: 626px; background: var(--card-navy); }

  .brand-name {
    position: absolute;
    font-weight: 600;
    color: var(--ink-white);
    text-align: center;
    line-height: 1.1;
    letter-spacing: 0.5px;
  }
  .card--front .brand-name {
    left: 30px;
    top: 112px;
    width: 180px;
    font-size: 24px;
  }
  .card--back .brand-name {
    left: 0;
    top: 100px;
    width: 100%;
    font-size: 34px;
  }

  .divider {
    position: absolute;
    left: 223px;
    top: 94px;
    width: 1px;
    height: 96px;
    background: var(--divider);
  }
  .person {
    position: absolute;
    left: 238px;
    top: 82px;
  }
  .person__name {
    font-size: 15.5px;
    font-weight: 600;
    letter-spacing: 0.6px;
    text-transform: uppercase;
    line-height: 20px;
  }
  .person__title {
    font-size: 13.5px;
    text-transform: uppercase;
    line-height: 20px;
  }
  .contacts {
    position: absolute;
    left: 238px;
    top: 145px;
    list-style: none;
    font-size: 12.5px;
    line-height: 17px;
  }
  .contacts li {
    display: flex;
    align-items: center;
    gap: 7px;
  }
  .contacts svg { width: 10px; height: 10px; fill: var(--ink-white); flex: none; }
  .tagline {
    position: absolute;
    left: 43px;
    top: 233px;
    font-family: "Noto Serif", Georgia, serif;
    font-size: 14px;
    letter-spacing: 0.4px;
    color: var(--ink-soft);
  }
</style>
</head>
<body>
<main class="stage">
  <section class="card card--front" aria-label="Business card front">
    <p class="brand-name">Kettle Mesa<br>Popcorn</p>
    <div class="divider"></div>
    <div class="person">
      <p class="person__name">Dale Whitcombe</p>
      <p class="person__title">Director</p>
    </div>
    <ul class="contacts">
      <li>
        <svg viewBox="0 0 10 10" aria-hidden="true"><path d="M1 3.2 Q1 1.5 2.5 1.5 H7.5 Q9 1.5 9 3.2 V4 H7 V3.2 H3 V4 H1 Z M2 5 L3.5 3.8 H6.5 L8 5 V8.5 H2 Z"/></svg>
        <span>+1 555 014 2286</span>
      </li>
      <li>
        <svg viewBox="0 0 10 10" aria-hidden="true"><path d="M1 2.5 H9 V7.5 H1 Z" fill="#fff"/><path d="M1 2.5 L5 5.5 L9 2.5" stroke="#9c232b" stroke-width="0.9" fill="none"/></svg>
        <span>Dale@kettlemesapopcorn.com</span>
      </li>
      <li>
        <svg viewBox="0 0 10 10" aria-hidden="true"><circle cx="5" cy="5" r="4.3"/><path d="M5 0.7 V9.3 M0.7 5 H9.3 M5 0.7 Q2.2 5 5 9.3 M5 0.7 Q7.8 5 5 9.3" stroke="#9c232b" stroke-width="0.7" fill="none"/></svg>
        <span>www.kettlemesapopcorn.com</span>
      </li>
    </ul>
    <p class="tagline">Crafted with a crunch</p>
  </section>

  <section class="card card--back" aria-label="Business card back">
    <p class="brand-name">Kettle Mesa<br>Popcorn</p>
  </section>
</main>
</body>
</html>
```